Mi ZOV Menu

I am attaching our menu itmes for our new fast casual business. I need to design a printable menu. Tri fold or bi fold depending on what fits. I want it to be easy to order but also look cool. If we can get a general design and I can add pictures if needed when I get them. For now they can be generic

Industry/Entity Type

Food

Font styles to use
Serif

Colors
0054AA
0677BA
7BADD7
CADEEF
E8F1F8

Requirements
Nice to have
• Some other businesses that have similar menus are redmaplediner.com and thelanternworks.com https://pelmorahouse.ca/en/food-menu/

```html
<!DOCTYPE html>
<html lang="en">
<head>
<meta charset="utf-8">
<title>Mi ZOV Menu</title>
<link href="https://fonts.googleapis.com/css2?family=Lilita+One&family=Montserrat:wght@400;500;600;700&display=swap" rel="stylesheet">
<style>
:root{
  --blue-deep:#0054AA;
  --blue-mid:#0677BA;
  --blue-soft:#7BADD7;
  --blue-pale:#CADEEF;
  --blue-mist:#E8F1F8;
  --paper:#f2f2f2;
  --ink:#2b2b2b;
  --backdrop:#0c2447;
}
*{box-sizing:border-box;margin:0;padding:0}
html,body{width:782px;height:1200px;overflow:hidden}
body{background:var(--backdrop);font-family:'Montserrat',sans-serif;position:relative}
.sheet{position:absolute;left:60px;width:662px;height:511px;display:flex}
.sheet--outside{top:62px}
.sheet--inside{top:627px}
.panel{position:relative;width:220.7px;height:100%;overflow:hidden}
.panel--blue{background:linear-gradient(160deg,var(--blue-deep) 0%,#0a4aa0 55%,var(--blue-deep) 100%);color:#fff}
.panel--paper{background:var(--paper);color:var(--ink)}
.heading{position:absolute;left:0;right:0;text-align:center;font-family:'Lilita One',sans-serif;color:var(--blue-deep);letter-spacing:.5px;line-height:1}
.heading--white{color:#fff}
.heading .soft{color:var(--blue-soft)}
.note{position:absolute;left:10px;right:10px;text-align:center;font-size:6.3px;font-weight:600;color:var(--blue-deep);line-height:1.3;text-transform:uppercase}
.panel--blue .note{color:var(--blue-soft)}
.item{position:absolute;left:14px;right:12px}
.item__name{font-size:9.6px;font-weight:600;text-transform:uppercase;line-height:1.3;padding-right:34px}
.item__desc{font-size:7.3px;line-height:1.5;padding-right:40px;margin-top:1px}
.price{position:absolute;right:0;top:-4px;width:26px;height:26px;background:var(--blue-soft);border-radius:6px 9px 5px 8px;display:flex;align-items:center;justify-content:center;font-size:7.6px;font-weight:600;color:var(--blue-deep)}
.panel--blue .price{color:var(--blue-deep)}
.price--low{top:2px}
.price--mid{top:6px}
.banner{position:absolute;left:20px;right:20px;background:var(--blue-soft);color:var(--ink);text-align:center;font-weight:600;border-radius:3px}
.photo{position:absolute}
.skewer-line{position:absolute;left:22px;right:10px;font-size:9.6px;font-weight:600;color:var(--blue-deep);line-height:1.35;text-transform:uppercase}
.lorem{position:absolute;left:24px;right:24px;text-align:center;font-size:7.2px;line-height:1.78;color:#fff}
</style>
</head>
<body>

<!-- Outside sheet -->
<section class="sheet sheet--outside">

  <div class="panel panel--blue">
    <h2 class="heading heading--white" style="top:12px;font-size:23px">MI ZOV <span class="soft">BOWLS</span></h2>
    <p class="note" style="top:37px">MIZOV Skepasti- served on pita w/ lettuce,<br>tomatoes, red onions &amp; ZOV mafia sauce</p>
    <div class="item" style="top:62px"><p class="item__name">Mi ZOV Add Gyro</p><span class="price">10.9</span></div>
    <div class="item" style="top:94px"><p class="item__name">Add Grilled Chicken</p><span class="price">10.9</span></div>
    <div class="item" style="top:126px"><p class="item__name">Add Pork Belly</p><span class="price">10.9</span></div>
    <div class="item" style="top:158px"><p class="item__name">Add Salmon</p><span class="price">10.9</span></div>
    <h2 class="heading heading--white" style="top:178px;font-size:22px">ENTRÉES</h2>
    <div class="item" style="top:214px"><p class="item__name">Gyro Platter</p><p class="item__desc">Served with Pita, Tzaziki, Rice &amp; Salad</p><span class="price price--low">12</span></div>
    <div class="item" style="top:246px"><p class="item__name">Pork Souvlaki Platter</p><p class="item__desc">Served with Pita, Tzaziki, Rice &amp; Salad</p><span class="price price--low">12</span></div>
    <div class="item" style="top:278px"><p class="item__name">Chicken Platter</p><p class="item__desc">Served with Pita, Tzaziki, Rice &amp; Salad</p><span class="price price--low">12</span></div>
    <div class="item" style="top:310px"><p class="item__name">Falalfal Platter</p><p class="item__desc">Served with Pita, Tzaziki, Rice &amp; Salad</p><span class="price price--low">12</span></div>
    <p class="banner" style="top:350px;font-size:7.6px;line-height:1.55;padding:3px 6px">MIZOV- ABOVE SERVED WITH PITA,<br>TZAZIKI, RICE &amp; GREEK SALAD</p>
    <div class="item" style="top:396px"><p class="item__name">Greek Style Half Roast<br>Chicken</p><p class="item__desc">Marinated in extra virgin olive oil &amp; herbs served with Greek Potatoes 19.5</p><span class="price price--mid">18.5</span></div>
    <div class="item" style="top:455px"><p class="item__name">Pastitsio</p><p class="item__desc">Greek pasta, seasoned ground beef topped w/Bechamel cream served w/ Greek potatoes</p><span class="price price--low">18.5</span></div>
  </div>

  <div class="panel panel--paper">
    <p class="note" style="top:12px">ZOV's Greek Mafia Burger<br>• "It's to die for" •<br>12<br>Egg, grilled onion, cheddar, tomatoes, pickled<br>jalapenos &amp; ZOV mafia sauce</p>
    <h2 class="heading" style="top:64px;font-size:22px">MI ZOV KIDS</h2>
    <div class="item" style="top:91px"><p class="item__name">Chicken Skewer</p><p class="item__desc">Served with fried and tzaziki</p><span class="price price--low">7</span></div>
    <div class="item" style="top:123px"><p class="item__name">Baked Salmon</p><p class="item__desc">Served with rice</p><span class="price price--low">12</span></div>
    <div class="item" style="top:155px"><p class="item__name">Little Mafia Burger</p><p class="item__desc">Single burger with little ZOV<br>mafia sauce with fries</p><span class="price price--low">8</span></div>
    <h2 class="heading" style="top:204px;font-size:22px">SIDES</h2>
    <div class="item" style="top:235px"><p class="item__name">Greek Oven Potatoes</p><span class="price">6</span></div>
    <div class="item" style="top:272px"><p class="item__name">Rice</p><span class="price">2</span></div>
    <div class="item" style="top:296px"><p class="item__name">Greek Style Green Beans<br>Baked in Tomato Sauce</p><span class="price price--low">6</span></div>
    <div class="item" style="top:328px"><p class="item__name">Pita</p><span class="price price--low">2</span></div>
    <svg class="photo" style="left:0;top:385px" width="221" height="126" viewBox="0 0 221 126" aria-hidden="true"><path d="M0 18 C30 6 55 16 80 8 C110 0 140 14 170 6 C195 0 210 10 221 4 L221 126 L0 126 Z" fill="var(--blue-soft)"/></svg>
    <div class="photo" role="img" aria-label="Plate of grilled chicken skewers with tzaziki and salad" style="left:72px;top:333px;width:70px;height:70px;border-radius:50%;background:radial-gradient(circle at 50% 45%,#e9e4da 0%,#c98f55 55%,#8a5a2e 100%)"></div>
    <h2 class="heading" style="top:410px;font-size:22px">SKEWERS</h2>
    <p class="skewer-line" style="top:441px">Chicken Souvlaki Skewers 10<br>Skewers 25.00 20 Skewers 50.00</p>
    <p class="skewer-line" style="top:473px">Pork Souvlaki Skewers 10<br>Skewers 25.00 20 Skewers 50.00</p>
  </div>

  <div class="panel panel--blue">
    <div class="photo" role="img" aria-label="Grilled chicken skewers on pita with lemon and a bowl of tzaziki" style="left:8px;top:0;width:213px;height:224px;border-radius:0 0 0 110px;background:radial-gradient(circle at 50% 35%,#f4f0e6 0%,#d9a86a 45%,#9b6432 80%,#0a4aa0 100%)"></div>
    <h2 class="heading heading--white" style="top:250px;font-size:30px">MI ZOV</h2>
    <p class="banner" style="top:290px;font-size:10px;padding:5px 0">Fresh Greek. Fast. Bold.</p>
    <p class="lorem" style="top:324px">Lorem ipsum dolor sit amet, consectetur adipiscing elit, sed do eiusmod tempor incidi dunt ut labore et dolore magna aliqua. Ut enim ad minim veniam, quis nostrud exercitation ullamco laboris nisi ut aliquip ex ea commodo consequat.</p>
    <div class="photo" role="img" aria-label="Two gyro wraps filled with meat and tzaziki" style="left:50px;top:409px;width:171px;height:85px;border-radius:40px 0 0 40px;background:linear-gradient(120deg,#e8d9bd 0%,#a86a3c 45%,#f0e6d2 70%,#9b5f33 100%)"></div>
  </div>
</section>

<!-- Inside sheet -->
<section class="sheet sheet--inside">

  <div class="panel panel--paper">
    <h2 class="heading" style="top:12px;font-size:22px">DIPS</h2>
    <div class="item" style="top:47px"><p class="item__name">Trio Dip Appetizer</p><p class="item__desc">Tzaziki, Hummus &amp; Tirokafteri served<br>with 2 Pitas</p><span class="price price--low">10.9</span></div>
    <div class="item" style="top:91px"><p class="item__name">Tzaziki Dip</p><p class="item__desc">Served w/ 2 pitas</p><span class="price price--low">10.9</span></div>
    <div class="item" style="top:131px"><p class="item__name">Tirokafteri Dip</p><p class="item__desc">Served with 2 pitas (spicy feta dip)</p><span class="price price--low">10.9</span></div>
    <div class="item" style="top:174px"><p class="item__name">Red Pepper Hummus Dip</p><p class="item__desc">Served w/ 2 pitas</p><span class="price price--low">10.9</span></div>
    <div class="photo" role="img" aria-label="Grilled pork souvlaki skewer" style="left:12px;top:218px;width:165px;height:60px;border-radius:30px;background:linear-gradient(90deg,rgba(242,242,242,0) 0%,#b98a60 25%,#8e5a35 60%,rgba(242,242,242,0) 100%)"></div>
    <h2 class="heading" style="top:295px;font-size:22px">STARTERS</h2>
    <div class="item" style="top:330px"><p class="item__name">Greek Gigantes Appetizer</p><p class="item__desc">Large white beans baked in a tomato based sauce topped with feta served w/ pita</p><span class="price price--low">10.9</span></div>
    <div class="item" style="top:383px"><p class="item__name">Dolmades</p><span class="price">9.5</span></div>
    <div class="item" style="top:414px"><p class="item__name">Greek Wings</p><p class="item__desc">Ladolemono &amp; feta; served w/tzaziki</p><span class="price price--low">13.5</span></div>
    <div class="item" style="top:466px"><p class="item__name">Phyllo Wrapped Feta</p><span class="price">10.9</span></div>
  </div>

  <div class="panel panel--paper">
    <div class="photo" role="img" aria-label="Bowl of quinoa salad with greens and avocado" style="left:39px;top:-30px;width:140px;height:113px;border-radius:0 0 70px 70px;background:radial-gradient(circle at 50% 30%,#c9b67a 0%,#5f8a3a 50%,#dfe3e6 85%)"></div>
    <h2 class="heading" style="top:103px;font-size:22px">FRIES</h2>
    <div class="item" style="top:131px"><p class="item__name">Seasoned Fries</p><p class="item__desc">Salt, Pepper, Oregano</p><span class="price price--low">5</span></div>
    <div class="item" style="top:162px"><p class="item__name">Feta Fries- Mi ZOV</p><p class="item__desc">Seasoned &amp; Feta</p><span class="price price--low">5</span></div>
    <div class="item" style="top:194px"><p class="item__name">Poutine Fries</p><p class="item__desc">Kasseri Cheese, Gyro</p><span class="price price--low">5</span></div>
    <div class="item" style="top:230px"><p class="item__name">Sauce Fries</p><p class="item__desc">Sauce</p><span class="price price--low">5</span></div>
    <h2 class="heading" style="top:263px;font-size:22px">SALADS</h2>
    <p class="note" style="top:289px;font-style:italic">ZOV: Gyro, chicken gyro, pork souvlaki<br>or grilled shrimp reg. +6.5/ lg.+8.5</p>
    <div class="item" style="top:313px"><p class="item__name">Village Salad- Mi ZOV</p><p class="item__desc">Cherry,tomatoes, cucumbers, Kalamata olives, red onions, green peppers, feta, capers, oregano &amp; Greek Vinaigrette</p><span class="price price--low">12.9</span></div>
    <div class="item" style="top:366px"><p class="item__name">Greek Salad-Mi ZOV</p><p class="item__desc">Romaine mixed green lettuce, tomatoes, cucumbers, onions, olives, pepperoncini, green peppers, Feta &amp; house dressing</p><span class="price price--low">9.9</span></div>
    <div class="item" style="top:418px"><p class="item__name">Marouli Salad</p><p class="item__desc">romaine lettuce, spring onions, dill, cherry tomatoes with kasseri cheese</p><span class="price price--mid">12</span></div>
    <div class="item" style="top:462px"><p class="item__name">Meditteranean Salad</p><p class="item__desc">Mixed green romaine lettuce, cherry tomatoes, olives, dried figs</p><span class="price price--mid">10.9</span></div>
  </div>

  <div class="panel panel--paper">
    <h2 class="heading" style="top:12px;font-size:22px">HANDHELD PITAS</h2>
    <p class="note" style="top:37px">MIZOV-Tomato, tzaziki, red onions, fries</p>
    <div class="item" style="top:55px"><p class="item__name">Gyro</p><p class="item__desc">Beef &amp; Lamb</p><span class="price price--low">10</span></div>
    <div class="item" style="top:87px"><p class="item__name">Shaved Pork Belly</p><span class="price price--low">10</span></div>
    <div class="item" style="top:119px"><p class="item__name">Grilled Chicken</p><span class="price price--low">10</span></div>
    <div class="item" style="top:151px"><p class="item__name">Falafal</p><p class="item__desc">Vegetarian</p><span class="price price--low">10</span></div>
    <div class="photo" role="img" aria-label="Falafel wraps with lettuce and avocado on a white tray" style="left:13px;top:181px;width:208px;height:159px;border-radius:60px 0 20px 20px;background:radial-gradient(circle at 60% 45%,#8a6a3a 0%,#d8c39a 40%,#6d9a45 70%,rgba(242,242,242,0) 100%)"></div>
    <h2 class="heading" style="top:355px;font-size:22px">SKEPASTI</h2>
    <p class="note" style="top:383px">MIZOV Skepasti- served on pita w/ lettuce,<br>tomatoes, red onions &amp; ZOV mafia sauce</p>
    <div class="item" style="top:411px"><p class="item__name">Gyro Club</p><span class="price">12</span></div>
    <div class="item" style="top:443px"><p class="item__name">Pork Belly Club</p><span class="price">12</span></div>
    <div class="item" style="top:475px"><p class="item__name">Grilled Chicken Club</p><span class="price">12</span></div>
  </div>
</section>

</body>
</html>
```